Professional Accounting Services Flyer

Attached is a publisher document and word document each containing the flyer text. This needs to be polished and improved to become an A4 2 sided marketing flyer.
It would be helpful if the design graphics on the flyer are in keeping with the product being sold, which is accounting and financial services.
The business in essence provides outsourced Chief Financial Office (CFO) services along with bookkeeping and a range of other accounting functions.

Target Market(s)

Small to Medium sized businesses requiring accounting support beyond the traditional preparation of tax returns

Industry/Entity Type

Accounting

Colors
0255a3
3277b5
85acd3
cedeed
ffffff
000000

Requirements
Must have
• The provided text
• Professional look and feel consistent with provision of professional accounting and financial services
• 2 sided A4 flyer
Nice to have
• Effective graphics which enhance the message and are in keeping with the theme of the business
Should not have
• Tacky or gimmicky looking graphics (please keep the graphics professional looking)
• A feel that indicates that tax return preparation is part of the business

```html
<!DOCTYPE html>
<html lang="en">
<head>
<meta charset="utf-8">
<title>Keystone Advisory – Flyer</title>
<link rel="stylesheet" href="https://fonts.googleapis.com/css2?family=Arimo:wght@400;700&display=swap">
<style>
:root{
  --navy:#0255a3;
  --blue:#3277b5;
  --sky:#85acd3;
  --mist:#cedeed;
  --white:#ffffff;
  --black:#000000;
  --ink:#3a3d42;
  --stage:#e4e9ef;
}
*{box-sizing:border-box;margin:0;padding:0}
html,body{width:1200px;height:900px;overflow:hidden}
body{background:var(--stage);font-family:"Arimo",Arial,sans-serif;color:var(--ink);position:relative}
.page{position:absolute;top:54px;width:560px;height:792px;overflow:hidden;box-shadow:0 2px 10px rgba(0,0,0,.18)}
.page--front{left:25px;background:linear-gradient(90deg,#ffffff 0%,#ffffff 48%,#eef1f5 100%)}
.page--back{left:615px;background:linear-gradient(180deg,#ffffff 20%,#e6ecf5 60%,#c9d6ea 100%)}
.header{position:absolute;left:0;top:0;width:560px}
.brand{position:absolute;font-weight:700;letter-spacing:.5px;white-space:nowrap}
.page--front .brand{left:0;width:560px;text-align:center;top:43px;font-size:38px;color:var(--white)}
.page--front .tagline{position:absolute;left:108px;top:85px;font-size:14.5px;color:var(--white);white-space:nowrap}
.page--back .brand{right:37px;top:37px;font-size:30px;color:#1a1a1a}
.page--back .tagline{position:absolute;right:37px;top:66px;font-size:12.5px;color:var(--blue);white-space:nowrap}
.col{position:absolute;font-size:8.3px;line-height:10.6px}
.col h2{font-size:10.6px;font-weight:400;color:var(--blue);margin:0 0 2px;line-height:12.5px}
.col p{margin:0 0 3px}
.col .q{font-weight:700;color:#222;margin-top:5px}
.col section{margin-bottom:12px}
.col ul{list-style:none;margin:0 0 4px}
.col li{position:relative;padding-left:10px;margin-bottom:2px}
.col li::before{content:"";position:absolute;left:1px;top:3px;width:4px;height:4px;border-radius:50%;background:var(--blue)}
.callout{color:var(--navy);text-align:center;font-size:9.6px;line-height:12px;margin:6px 0 12px}
.lead{font-size:9.4px;color:#222;margin:3px 0 2px}
.cfo-box{position:absolute;left:23px;top:525px;width:242px;height:243px;border:2px solid var(--white);border-radius:12px;background:var(--mist);box-shadow:0 1px 5px rgba(0,0,0,.25);font-size:8.3px;line-height:10.6px}
.cfo-box h2{background:var(--navy);color:var(--white);font-size:11px;font-weight:400;padding:4px 12px;margin:-2px -2px 8px;border-radius:12px 0 0 0}
.cfo-box .inner{padding:0 10px}
.cfo-box p{margin:0 0 4px}
.cfo-box ul{list-style:none}
.cfo-box li{position:relative;padding-left:10px;margin-bottom:1.6px}
.cfo-box li::before{content:"";position:absolute;left:1px;top:3px;width:4px;height:4px;border-radius:50%;background:var(--blue)}
.photo-tablet{position:absolute;left:279px;top:560px;width:281px;height:232px;background:linear-gradient(200deg,#ffffff 0%,#e7edf5 35%,#b9c9dd 70%,#8ea6c4 100%)}
.contact-box{position:absolute;left:290px;top:675px;width:270px;height:92px;background:rgba(60,62,66,.82);border-radius:10px 0 0 10px;color:var(--white);text-align:right;padding:9px 14px 0 0;font-size:12.4px;line-height:18.4px;white-space:nowrap}
.front-footer{position:absolute;left:0;bottom:0;width:560px;height:24px;background:linear-gradient(90deg,#cfd9e6,#8fa8c8)}
.back-footer{position:absolute;left:0;bottom:0;width:560px;height:54px;background:var(--black);border-top:3px solid var(--navy);color:var(--white);font-size:10.5px;display:flex;justify-content:space-between;align-items:center;padding:0 22px 0 26px;white-space:nowrap}
.divider{position:absolute;width:1px;background:#d5dbe3}
</style>
</head>
<body>

<article class="page page--front">
  <svg class="header" width="560" height="130" viewBox="0 0 560 130">
    <defs>
      <linearGradient id="towerTone" x1="0" y1="0" x2="1" y2="1">
        <stop offset="0" stop-color="#2a5f9e"/>
        <stop offset=".5" stop-color="#5b8fc4"/>
        <stop offset="1" stop-color="#1d4c86"/>
      </linearGradient>
    </defs>
    <rect width="560" height="130" fill="url(#towerTone)" role="img" aria-label="Photo of glass office towers against the sky"/>
    <path d="M0,108 Q280,90 560,98 L560,130 L0,130 Z" fill="var(--navy)"/>
    <path d="M0,118 Q280,100 560,106 L560,130 L0,130 Z" fill="var(--white)"/>
  </svg>
  <div class="brand">KEYSTONE ADVISORY</div>
  <div class="tagline">Provide outsourced solutions to your business.</div>

  <div class="col" style="left:35px;top:158px;width:238px">
    <section>
      <h2>Why Choose Keystone Advisory?</h2>
      <ul>
        <li>Are you experiencing significant growth and facing pressure to continue to successfully manage all aspects of your business?</li>
        <li>Do you find the day to day tasks of meeting your financial, accounting and company secretarial obligations is diverting your time from your core business?</li>
        <li>Is a lack of expert financial support holding your business back from achieving its potential?</li>
        <li>Are you considering listing, raising capital, or borrowing funds to achieve your business goals?</li>
        <li>Are you looking for cost effective solutions to improve your business performance?</li>
      </ul>
      <p class="callout">If this is you Keystone Advisory may be able to help you achieve these goals.</p>
    </section>
    <section>
      <h2>What Services Does Keystone Advisory Provide?</h2>
      <p>Keystone Advisory is focused on providing outsourced solutions to your business.</p>
      <p class="lead">We specialise in the following areas:</p>
      <ul>
        <li>CFO services</li>
        <li>Company Secretarial services</li>
        <li>Financial Reporting</li>
        <li>Forensic Accounting</li>
        <li>Bookkeeping and Payroll</li>
      </ul>
    </section>
  </div>

  <div class="photo-tablet" role="img" aria-label="Photo of a hand touching a tablet showing financial charts"></div>
  <div class="front-footer"></div>

  <div class="cfo-box">
    <h2>CFO Services</h2>
    <div class="inner">
      <p>Large companies utilise the services of a Chief Financial Officer (CFO) to manage the financial complexity of modern businesses.</p>
      <p>CFO services allows you to have access to the same skills on a part time basis.</p>
      <p>This function allows you to have a senior financial professional assist with managing activities such as:</p>
      <ul>
        <li>Strategy development and execution</li>
        <li>Organisational structure optimisation</li>
        <li>Insurance Management</li>
        <li>Managing the financial team</li>
        <li>Planning and budgeting</li>
        <li>Debt and Capital raisings</li>
        <li>Negotiations with financial institutions</li>
        <li>Implementation of financial systems, policies and procedures</li>
      </ul>
    </div>
  </div>

  <div class="col" style="left:297px;top:158px;width:240px">
    <section>
      <h2>Company Secretarial Services</h2>
      <p>We can provide secretarial services whether your business is a private company just requiring the basics or if you operate a small capital listed entity requiring the services of a Company Secretary to meet the obligations of the Registry Board as well as Westex.</p>
    </section>
    <section>
      <h2>Financial Reporting</h2>
      <p>Whether you need to meet the expectations of banks or outside investors we can assist by providing the necessary skills to compile financial reports.</p>
      <p>Alternatively you may need assistance meeting the tight deadlines associated with raising funds through debt and equity markets.</p>
      <p>We can provide this service along with assistance in the preparation of Prospectus documents or Information Memorandum.</p>
      <p>We are able to act as lead or provide supplemental support for an existing internal team.</p>
    </section>
    <section>
      <h2>Forensic Accounting</h2>
      <p>Everyone hopes their employees are honest and act with integrity, however, this is not always the case.</p>
      <p>If your business has been the subject of a suspected financial crime we can help.</p>
      <p>We can conduct a forensic review and where needed provide expert testimony should the matter lead to a court case.</p>
    </section>
    <section>
      <h2>Bookkeeping and Payroll</h2>
      <p>These essential tasks form part of running every business but often take up an excessive amount of your valuable time.</p>
      <p>These tasks which are necessary can be performed by someone with the right skills allowing you to focus on the business.</p>
      <p>We can assist you with this enabling you to concentrate on the areas of your business that add the most value.</p>
    </section>
  </div>

  <div class="contact-box">
    Contact us:<br>
    Phone: 0400 555 018<br>
    Email: dharwood@keystonemail.com.au<br>
    Mail: PO Box 100 NORTHVALE WA 6000
  </div>
</article>

<article class="page page--back">
  <svg class="header" width="560" height="118" viewBox="0 0 560 118">
    <defs>
      <linearGradient id="chartTone" x1="0" y1="0" x2="1" y2="0">
        <stop offset="0" stop-color="#a9c3e2"/>
        <stop offset=".4" stop-color="#e4ecf6"/>
        <stop offset="1" stop-color="#ffffff"/>
      </linearGradient>
    </defs>
    <rect width="560" height="118" fill="url(#chartTone)" role="img" aria-label="Photo of a printed bar chart with a pen and glasses"/>
    <path d="M0,98 Q280,80 560,86 L560,118 L0,118 Z" fill="var(--navy)"/>
    <path d="M0,108 Q280,90 560,94 L560,118 L0,118 Z" fill="var(--white)"/>
  </svg>
  <div class="brand">KEYSTONE ADVISORY</div>
  <div class="tagline">Provide outsourced solutions to your business.</div>

  <div class="divider" style="left:280px;top:140px;height:590px"></div>

  <div class="col" style="left:36px;top:152px;width:234px">
    <section>
      <h2>About Keystone Advisory</h2>
      <p>Keystone Advisory is focused on delivering services to small and medium businesses which are often only available to larger businesses.</p>
      <p>At its core Keystone Advisory is focused on providing to small and medium sized businesses the key services large organisations gain through the employment of a dedicated CFO.</p>
      <p>These services will enable you to focus your efforts on growing your business and ensuring the operations are performing to achieve the goals you have set.</p>
      <p>Keystone Advisory is able to partner with you to ensure that as the business grows, the financial and governance needs continue to keep pace and enable growth to occur efficiently and effectively.</p>
      <p>With growth and size comes complexity and Keystone Advisory is able assist you in managing these risks allowing the business to thrive and develop successfully.</p>
    </section>
    <section>
      <h2>Key Management</h2>
      <p>Daniel Harwood is at the heart of the business with over 25 years of experience gained across both public practice and commerce.</p>
      <p>Most of this experience has been gained working in a range of commercial organisations ranging in size from 100 staff through to organisations with over 10,000 employees.</p>
      <p>This has included senior financial positions within Westex 200 companies with operations both within Australia and operations overseas.</p>
      <p>Daniel's experience extends to a range of sectors, including retailing, wholesaling, mining and exploration, construction and manufacturing.</p>
      <p>This experience is particularly extensive within fast moving consumer goods and operational mines extracting gold, copper and coal.</p>
      <p>Daniel has also been involved in a range of corporate activities including business acquisitions, stock exchange listings (particularly in Singapore), debt raisings and corporate demergers.</p>
      <p>Through these activities, he has been exposed to the debt and equity market regimes in Australia, Singapore and the United States of America.</p>
    </section>
  </div>

  <div class="col" style="left:294px;top:152px;width:236px">
    <h2>Frequently Asked Questions</h2>
    <p class="q" style="margin-top:0">If I utilise the CFO services of Keystone Advisory, does that mean I don't need to worry about the financials?</p>
    <p>Keystone Advisory acts as your personal CFO.</p>
    <p>Like any successful business the CEO must remain engaged with the financial health and prosperity of the business.</p>
    <p>What Keystone Advisory will do, is assist you in fully understanding this information and using financial information to drive your business forward.</p>
    <p class="q">If I decide to raise capital or list my business on a stock exchange, can Keystone Advisory help me?</p>
    <p>Yes, there are a number of ways we can be of assistance.</p>
    <p>Keystone Advisory can act as your CFO and drive the process, including, managing the various aspects involved in raising capital and listing a company.</p>
    <p>If you already have internal resources but require additional help to achieve the outcome within the deadlines, Keystone Advisory can provide that assistance.</p>
    <p class="q">Does Keystone Advisory provide taxation services?</p>
    <p>While Keystone Advisory does not provide taxation services, we are able to assist you through an associate who is a registered tax agent.</p>
    <p class="q">Does Keystone Advisory conduct audit and assurance services?</p>
    <p>These services are not provided by Keystone Advisory, however there are a range of accounting firms we can direct you toward.</p>
    <p>We are also able to act in the same manner as a dedicated CFO would in engaging with these providers and managing the audit process should you require.</p>
    <p class="q">Does Keystone Advisory provide expert opinions for debt and equity raisings or takeovers?</p>
    <p>These are specialised services which Keystone Advisory does not provide.</p>
    <p>However, we can manage the process on your behalf to achieve the outcomes required.</p>
    <p class="q">Does Keystone Advisory provide Valuations?</p>
    <p>Keystone Advisory does not provide valuations, however, we are able to manage this process on your behalf or assist with collation of all relevant information to facilitate a valuation.</p>
  </div>

  <footer class="back-footer">
    <span>Phone: 0400 555 018</span>
    <span>Email: dharwood@keystonemail.com.au</span>
    <span>Mail: PO Box 100 NORTHVALE WA 6000</span>
  </footer>
</article>

</body>
</html>
```